Manifesto

I want a manifesto with the following five manifestos for our Not for Profit

- We are a For-purpose organisation
- Every service we offer is free
- Every product we sell funds our services
- Every financial transaction is transparent
- Our service is for the greater good
- Our purpose is always to serve the people
- We are a for purpose organisation

Its to go with this website logo/look/feel www.brightlantern.co.nz

Two attachments:

1. I quite like this look/feel of a manifesto (see attached), I want something clean, professional but I also quite like either Retro modern look feel also like a fresh, and uplifting as its for sick people coming to see us and our funds where anyone buys a product are used for helping those who are sick with healing......so needs something conveyed that is fresh, uplifing yet professional.
2. This attachment is how I wrote this down when inspired of how I wanted Bright Lantern to operate. This is our values chart. It has to say

Also check out our website for our logo, look etc.. it doesnt have to be the same but red somewhere would link back to logo. www.brightlantern.co.nz .

```html
<!DOCTYPE html>
<html lang="en">
<head>
<meta charset="utf-8">
<title>Bright Lantern Manifesto</title>
<link rel="stylesheet" href="https://fonts.googleapis.com/css2?family=Alfa+Slab+One&family=Montserrat:ital,wght@0,300;0,400;0,500;0,700;0,800;1,300;1,800&family=Great+Vibes&display=swap">
<style>
  :root {
    --paper: #f7f7f7;
    --plaque: #2b2a2c;
    --blue: #2a86c8;
    --red: #d8202a;
    --white: #ffffff;
  }
  html, body {
    margin: 0;
    padding: 0;
    width: 923px;
    height: 1200px;
    overflow: hidden;
    background: var(--paper);
  }
  .manifesto {
    display: block;
    width: 923px;
    height: 1200px;
  }
  .plaque { fill: var(--plaque); }
  .plaque-rule { fill: none; stroke: var(--white); stroke-width: 2; }
  .band { fill: var(--blue); }
  .band-frame { fill: none; stroke: var(--white); stroke-width: 2; }
  .sans { font-family: "Montserrat", sans-serif; }
  .slab { font-family: "Alfa Slab One", serif; }
  .script { font-family: "Great Vibes", cursive; }
  .white { fill: var(--white); }
  .red { fill: var(--red); }
  .kicker { font-size: 21px; font-weight: 400; letter-spacing: 1px; }
  .headline { font-size: 39px; font-weight: 800; }
  .title { font-size: 62px; font-weight: 500; }
  .statement { font-size: 30px; font-weight: 400; letter-spacing: 0.5px; }
  .statement-strong { font-weight: 700; }
  .pillar { font-size: 16.5px; letter-spacing: 0.2px; }
  .service { font-size: 29px; font-weight: 800; font-style: italic; }
  .joiner { font-size: 9px; font-weight: 500; }
  .good { font-size: 29px; font-weight: 300; font-style: italic; }
  .lead { font-size: 15px; font-weight: 500; letter-spacing: 0.5px; }
  .motto { font-size: 70px; }
  .tail { font-size: 17px; font-weight: 500; letter-spacing: 1px; }
  .signoff { font-size: 28px; }
  .brand-name { font-size: 25px; font-weight: 700; }
</style>
</head>
<body>
<svg class="manifesto" viewBox="170 250 580 790" role="img" aria-label="Bright Lantern manifesto">
  <!-- plaque with notched corners -->
  <path class="plaque" d="M237 263 H682 A40 40 0 0 0 722 303 V988 A40 40 0 0 0 682 1028 H237 A40 40 0 0 0 197 988 V303 A40 40 0 0 0 237 263 Z"/>
  <path class="plaque-rule" d="M239 275 H680 A30 30 0 0 0 710 305 V986 A30 30 0 0 0 680 1016 H239 A30 30 0 0 0 209 986 V305 A30 30 0 0 0 239 275 Z"/>

  <g class="slanted" transform="translate(460 0) skewY(-7.8)">
    <!-- heading -->
    <text class="sans white kicker" x="-172" y="298">WE ARE</text>
    <text class="sans red headline" x="-178" y="344">A FOR PURPOSE</text>

    <!-- organisation banner -->
    <rect class="band" x="-282" y="357" width="564" height="95"/>
    <rect class="band-frame" x="-268" y="366" width="536" height="77"/>
    <text class="sans white title" x="0" y="427" text-anchor="middle">ORGANISATION</text>

    <text class="sans white statement" x="0" y="494" text-anchor="middle">EVERY <tspan class="red statement-strong">SERVICE</tspan> IS <tspan class="statement-strong">FREE</tspan></text>

    <!-- pillars banner -->
    <rect class="band" x="-282" y="510" width="564" height="140"/>
    <rect class="band-frame" x="-268" y="519" width="536" height="122"/>
    <line class="band-frame" x1="0" y1="519" x2="0" y2="641"/>
    <text class="slab white pillar" text-anchor="middle">
      <tspan x="-140" y="562">EVERY <tspan class="red">PRODUCT</tspan></tspan>
      <tspan x="-140" y="584">WE SELL</tspan>
      <tspan x="-140" y="606">FUNDS OUR SERVICES</tspan>
    </text>
    <text class="slab white pillar" text-anchor="middle">
      <tspan x="135" y="562">EVERY <tspan class="red">FINANCIAL</tspan></tspan>
      <tspan x="135" y="584">TRANSACTION</tspan>
      <tspan x="135" y="606">IS <tspan class="red">TRANSPARENT</tspan></tspan>
    </text>

    <!-- service banner -->
    <rect class="band" x="-282" y="669" width="564" height="84"/>
    <rect class="band-frame" x="-268" y="678" width="536" height="66"/>
    <text class="sans red service" x="-28" y="721" text-anchor="end">OUR SERVICE</text>
    <text class="sans white joiner" x="-12" y="709" text-anchor="middle">IS</text>
    <text class="sans white joiner" x="-12" y="721" text-anchor="middle">FOR</text>
    <text class="sans white good" x="4" y="719">GREATER GOD</text>

    <!-- purpose banner -->
    <rect class="band" x="-282" y="772" width="564" height="138"/>
    <rect class="band-frame" x="-268" y="794" width="536" height="95"/>
    <rect class="band" x="-90" y="784" width="180" height="20"/>
    <rect class="band" x="-88" y="879" width="176" height="22"/>
    <text class="sans red lead" x="0" y="800" text-anchor="middle">SERVING PEOPLE</text>
    <text class="slab white motto" x="0" y="868" text-anchor="middle" textLength="345" lengthAdjust="spacingAndGlyphs">IS ALWAYS</text>
    <text class="sans white tail" x="0" y="896" text-anchor="middle">OUR PURPOSE</text>
  </g>

  <!-- sign-off -->
  <text class="script white signoff" x="320" y="978">We are</text>
  <circle class="red" cx="440" cy="966" r="8"/>
  <text class="sans red brand-name" x="456" y="975">Bright Lantern</text>
</svg>
</body>
</html>
```